Book cover needed for self help business book

Book cover needed and I will provide back cover blurb and barcode to the winning designer. Book may be too small for spine, but I will give you the page number details to confirm. Book information below:

Title: Nine Winters a Trader
Subtitle: Proven Market Methods That Keep Paying Off Now
Author: Maribel Okonte

Design should be clean, modern, and bold—something that appeals to everyday entrepreneurs and resellers. The cover should reflect grit, real-world hustle, and long-term wisdom without looking overly corporate or flashy. I am open to your creative ideas.

I am open to modern designs, but also designs of rugged old covers that simulate a book that may have aged over the years.

I prefer not to have pictures or silhouettes of people

Requirements
Nice to have
• I am open to modern designs, but also designs of rugged old covers that simulate a book that may have aged over the years.
Should not have
• Pictures or silhouettes of people

```html
<!DOCTYPE html>
<html lang="en">
<head>
<meta charset="UTF-8">
<title>Nine Winters a Trader — Book Cover</title>
<link rel="stylesheet" href="https://fonts.googleapis.com/css2?family=Oswald:wght@400;500;600&display=swap">
<style>
  :root {
    --backdrop: #4f6e96;
    --cover: #ffffff;
    --ink: #111111;
    --rule: #222222;
  }
  * { margin: 0; padding: 0; box-sizing: border-box; }
  html, body {
    width: 1200px;
    height: 900px;
    overflow: hidden;
    background: var(--backdrop);
  }
  .stage {
    width: 1200px;
    height: 900px;
    display: flex;
    align-items: center;
    justify-content: center;
  }
  .book-cover {
    width: 500px;
    height: 790px;
    background: var(--cover);
    padding: 80px 52px 0 62px;
    color: var(--ink);
    font-family: "Oswald", "Arial Narrow", sans-serif;
    display: flex;
    flex-direction: column;
  }
  .title {
    font-weight: 600;
    font-size: 96px;
    line-height: 1.02;
    text-transform: uppercase;
    letter-spacing: -0.5px;
  }
  .title span { display: block; }
  .rule-long {
    height: 2px;
    background: var(--rule);
    margin: 22px 0 18px;
    width: 100%;
  }
  .subtitle {
    font-weight: 500;
    font-size: 22px;
    line-height: 1.7;
    text-transform: uppercase;
    letter-spacing: 0.3px;
  }
  .rule-short {
    height: 2px;
    background: var(--rule);
    margin: 16px 0 26px;
    width: 140px;
  }
  .author {
    font-weight: 500;
    font-size: 50px;
    line-height: 1;
    text-transform: uppercase;
    letter-spacing: 0.3px;
  }
</style>
</head>
<body>
  <main class="stage">
    <article class="book-cover">
      <h1 class="title">
        <span>Nine</span>
        <span>Winters a</span>
        <span>Trader</span>
      </h1>
      <div class="rule-long"></div>
      <p class="subtitle">Proven Market Methods That<br>Keep Paying Off Now</p>
      <div class="rule-short"></div>
      <p class="author">Maribel Okonte</p>
    </article>
  </main>
</body>
</html>
```